Business card design for Kovantrix

I need a business card based on the logo design produced for Kovantrix. The company is focused on triathlon and endurance sport coaching and the tag line is (per the logo) "Strength. Focus. Momentum". The design should be sophisticated, appropriate to an affluent and business oriented target market. Colors are optional but the color of the logo probably dictates the color used on the card. I envisage using the red logo, with black print for the wording and contact numbers on a white or cream background, but am open to alternative suggestions. I expect to select something fairly conventional, but would like to see some designs that are less conventional to stretch my thinking on what could be appropriate. I am assuming a single side design is best, but willing to consider double sided as an option.

Target Market(s)

Individual athletes and corporate health and wellness leaders

Industry/Entity Type

Health And Wellness

Contact Information for Business Card

The card should provide the following information:
Logo
My name: Marcus Bellingham
Company website: Kovantrix.com
My email: marcus.bellingham@kovantrix.com
My cell phone number: +1-555-812-6093

Font styles to use
Sans Serif

Colors

Designer to choose colors to be used in the design.

Requirements
Must have
• Space on the card - simple design, not over crowded.
Nice to have
• clean and clear font, nothing garish or mass market like
Should not have
• Do not add pictures

```html
<!DOCTYPE html>
<html lang="en">
<head>
<meta charset="utf-8">
<title>Kovantrix Business Card</title>
<link href="https://fonts.googleapis.com/css2?family=Questrial&display=swap" rel="stylesheet">
<style>
  :root {
    --brand-red: #b0282c;
    --ink: #1b1b1b;
    --paper: #ffffff;
    --backdrop: #e4e4e6;
  }
  * { margin: 0; padding: 0; box-sizing: border-box; }
  html, body {
    width: 1200px;
    height: 800px;
    overflow: hidden;
    background: var(--backdrop);
    font-family: "Questrial", "Century Gothic", sans-serif;
  }
  .canvas {
    width: 1200px;
    height: 800px;
    display: flex;
    align-items: center;
    justify-content: center;
    gap: 40px;
  }
  .card {
    position: relative;
    width: 540px;
    height: 309px;
    box-shadow: 0 6px 18px rgba(0,0,0,0.12);
  }
  .card--front { background: var(--paper); }
  .card--back {
    background: var(--brand-red);
    display: flex;
    align-items: center;
    justify-content: center;
  }
  .holder { position: absolute; left: 36px; top: 34px; }
  .holder__name { font-size: 19px; color: var(--ink); letter-spacing: 0.2px; }
  .holder__title { font-size: 13px; color: var(--brand-red); margin-top: 3px; }
  .contact {
    position: absolute;
    left: 36px;
    top: 172px;
    list-style: none;
  }
  .contact__item {
    display: flex;
    align-items: center;
    gap: 9px;
    font-size: 12px;
    color: var(--ink);
    height: 19px;
  }
  .contact__icon {
    width: 12px;
    height: 12px;
    fill: none;
    stroke: var(--brand-red);
    stroke-width: 1.2;
    flex: none;
  }
  .wordmark { text-align: center; line-height: 1; }
  .wordmark__name { font-size: 50px; letter-spacing: -0.5px; }
  .wordmark__tagline { font-size: 12px; letter-spacing: 0.6px; text-transform: uppercase; margin-top: 8px; }
  .card--front .wordmark {
    position: absolute;
    left: 280px;
    top: 120px;
    width: 230px;
    color: var(--brand-red);
  }
  .card--front .wordmark__tagline { color: var(--ink); font-size: 11px; }
  .card--back .wordmark { color: var(--paper); }
  .card--back .wordmark__name { font-size: 62px; }
  .card--back .wordmark__tagline { font-size: 14px; margin-top: 10px; }
  .rule { position: absolute; top: 270px; height: 2px; }
  .rule--ink { left: 0; width: 230px; background: var(--ink); }
  .rule--accent { left: 230px; right: 0; background: var(--brand-red); }
</style>
</head>
<body>
<main class="canvas">
  <section class="card card--front" aria-label="Business card front">
    <div class="holder">
      <p class="holder__name">Marcus Bellingham</p>
      <p class="holder__title">Managing Director</p>
    </div>
    <ul class="contact">
      <li class="contact__item">
        <svg class="contact__icon" viewBox="0 0 12 12" aria-hidden="true"><rect x="2.8" y="0.6" width="6.4" height="10.8" rx="1"/><line x1="5" y1="9.4" x2="7" y2="9.4"/></svg>
        +1-555-812-6093
      </li>
      <li class="contact__item">
        <svg class="contact__icon" viewBox="0 0 12 12" aria-hidden="true"><rect x="0.6" y="2.2" width="10.8" height="7.6"/><polyline points="0.6,2.6 6,6.6 11.4,2.6"/></svg>
        Kovantrix.com
      </li>
      <li class="contact__item">
        <svg class="contact__icon" viewBox="0 0 12 12" aria-hidden="true"><circle cx="6" cy="6" r="5.3"/><ellipse cx="6" cy="6" rx="2.3" ry="5.3"/><line x1="0.7" y1="6" x2="11.3" y2="6"/></svg>
        marcus.bellingham@kovantrix.com
      </li>
    </ul>
    <div class="wordmark">
      <p class="wordmark__name">Kovantrix</p>
      <p class="wordmark__tagline">Strength. Focus. Momentum</p>
    </div>
    <span class="rule rule--ink"></span>
    <span class="rule rule--accent"></span>
  </section>
  <section class="card card--back" aria-label="Business card back">
    <div class="wordmark">
      <p class="wordmark__name">Kovantrix</p>
      <p class="wordmark__tagline">Strength. Focus. Momentum</p>
    </div>
  </section>
</main>
</body>
</html>
```